Halvorn Hire Business Card Design

Need business cards designed for our new equipment rental. We specialize in renting to landscape / tree professionals, contractors, Do-It-Yourself'ers and Around the home or office. Looking for a eye catching card. Landscape and construction should be the theme. The logo is attached, and you can see our colors from the logo. You can use whatever color goes with it ok.

Target Market(s)

First off Landscape and Tree Professional. Then contractors, Do-It-Yourself'ers and rentals for Around the home or office.

Industry/Entity Type

Business

Contact Information for Business Card

Eye catching background that blends landscaping with construction equipment

Requirements
Must have
• Name on Card will Be: Derek Pollard (Manager)
• My Direct Phone Number is: 352-418-7093
• derek@halvornhire.example
• www.halvornhire.example
• 4172 Wexley Mill Road,
• Dade City FL 33590
Nice to have
• Would be Nice to have these bullets on the Face of the card that does not have all my information.
• Serving:
• Landscape / Tree Professionals
• Contractors
• DYI'ers or say Do-It-Yourself'ers
• Maybe have serving small and centered above these bullets, and these 3 bullets along the bottom of the card. Ideas?

```html
<!DOCTYPE html>
<html lang="en">
<head>
<meta charset="utf-8">
<title>Halvorn Hire — Business Card</title>
<link rel="stylesheet" href="https://fonts.googleapis.com/css2?family=Barlow+Semi+Condensed:wght@600;700&family=Open+Sans:wght@400;600&display=swap">
<style>
  :root {
    --page-bg: #d9d6d2;
    --card-bg: #efeeec;
    --navy: #1d3f5c;
    --ink: #1e1e1e;
    --amber: #e39c3a;
    --machine-grey: rgba(88, 92, 98, 0.42);
    --stripe: #fbfbfa;
  }
  * { margin: 0; padding: 0; box-sizing: border-box; }
  html, body {
    width: 1200px; height: 1054px; overflow: hidden;
    background: var(--page-bg);
  }
  .card {
    position: absolute; left: 150px; top: 270px;
    width: 900px; height: 514px;
    background: var(--card-bg);
    border-radius: 6px;
    overflow: hidden;
    box-shadow: 0 10px 30px rgba(0,0,0,0.15);
    font-family: "Open Sans", Arial, sans-serif;
  }
  .card-art { position: absolute; inset: 0; }
  .brand {
    position: absolute; left: 44px; top: 140px;
    display: flex; align-items: center; gap: 14px;
    font-family: "Barlow Semi Condensed", "Arial Narrow", sans-serif;
    font-weight: 700; font-size: 58px; color: var(--navy);
    letter-spacing: 1px;
  }
  .brand-dot {
    width: 22px; height: 22px; border-radius: 50%;
    background: var(--amber);
  }
  .person { position: absolute; left: 44px; top: 266px; }
  .person-name {
    font-family: "Barlow Semi Condensed", "Arial Narrow", sans-serif;
    font-weight: 600; font-size: 31px; color: var(--navy);
  }
  .person-role { font-size: 21px; color: var(--navy); margin-top: 2px; }
  .serving {
    position: absolute; left: 44px; top: 388px;
    color: var(--navy); font-size: 15px; line-height: 22px;
  }
  .serving-title { font-weight: 600; text-transform: uppercase; letter-spacing: 1.5px; font-size: 13px; margin-bottom: 3px; }
  .serving-list { list-style: none; }
  .serving-list li { display: flex; align-items: center; gap: 8px; }
  .serving-list li::before {
    content: ""; width: 6px; height: 6px; border-radius: 50%;
    background: var(--amber); flex: none;
  }
  .contact {
    position: absolute; right: 44px; top: 296px;
    text-align: right; color: var(--ink); font-size: 22px; line-height: 29px;
  }
  .address { margin-bottom: 14px; }
  .contact-line { display: flex; justify-content: flex-end; align-items: center; gap: 14px; }
  .contact-line svg { width: 20px; height: 20px; flex: none; }
</style>
</head>
<body>
  <div class="card">
    <svg class="card-art" viewBox="0 0 900 514" width="900" height="514">
      <polygon points="395,390 900,128 900,514 460,514" fill="var(--stripe)"/>
      <polygon points="412,384 900,140 900,514 474,514" fill="var(--amber)"/>
      <polygon role="img" aria-label="Large excavator arm and bucket silhouette sweeping across the card"
               points="300,352 300,508 420,508 900,90 900,0 820,0" fill="var(--machine-grey)"/>
    </svg>

    <div class="brand"><span class="brand-dot"></span>Halvorn Hire</div>

    <div class="person">
      <div class="person-name">Derek Pollard</div>
      <div class="person-role">Manager</div>
    </div>

    <div class="serving">
      <div class="serving-title">Serving</div>
      <ul class="serving-list">
        <li>Landscape / Tree Professionals</li>
        <li>Contractors</li>
        <li>Do-It-Yourself'ers</li>
      </ul>
    </div>

    <div class="contact">
      <div class="address">
        4172 Wexley Mill Road,<br>
        Dade City FL 33590
      </div>
      <div class="contact-line">352-418-7093
        <svg viewBox="0 0 20 20"><path d="M3 7c0-2 3-3 7-3s7 1 7 3v1h-4V6.5H7V8H3z M5 9h10l2 7H3z" fill="var(--ink)"/><circle cx="10" cy="12.5" r="2" fill="var(--amber)"/></svg>
      </div>
      <div class="contact-line">derek@halvornhire.example
        <svg viewBox="0 0 20 20"><g fill="none" stroke="var(--ink)" stroke-width="1.5"><circle cx="10" cy="10" r="7.5"/><ellipse cx="10" cy="10" rx="3.5" ry="7.5"/><path d="M2.5 10h15M4 6h12M4 14h12"/></g></svg>
      </div>
      <div class="contact-line">www.halvornhire.example
        <svg viewBox="0 0 20 20"><rect x="2" y="5" width="16" height="11" fill="var(--ink)"/><path d="M2 5l8 6 8-6" fill="none" stroke="var(--amber)" stroke-width="1.4"/></svg>
      </div>
    </div>
  </div>
</body>
</html>
```